Chiropractic Flyers to be made more up to date

I have used this series of flyers for my own practice. I would like the graphics to be brought up to date and the name of the doctor and the practice, the address, phone number and date to be removed and a blank box inserted in one place on the flyer that other chiropractors could use to personalize the flyers for their practice. On some of the flyers, this information is in several places. I'd like to have it all in one space so that it would be easy for the doctor to add it in their practice. They all need to be bright and colorful with catchy graphics.

Industry/Entity Type

Doctor

```html
<!DOCTYPE html>
<html lang="en">
<head>
<meta charset="utf-8">
<title>Wanted – Chiropractic Flyer</title>
<link rel="stylesheet" href="https://fonts.googleapis.com/css2?family=Alfa+Slab+One&family=Oswald:wght@500&display=swap">
<style>
  :root {
    --backdrop: #e7e4de;
    --frame: #5f5f5f;
    --paper-light: #f8ecd6;
    --paper-mid: #f1dfbf;
    --paper-edge: #e6d0a8;
    --ink: #2b2a28;
    --banner: #ffffff;
    --banner-fold: #d9cdb6;
    --art: #2e2d2b;
  }
  * { box-sizing: border-box; margin: 0; padding: 0; }
  html, body {
    width: 900px; height: 1200px; overflow: hidden;
    background: var(--backdrop);
  }
  .flyer {
    position: absolute; left: 88px; top: 86px;
    width: 744px; height: 1040px;
    background: var(--frame);
    padding: 22px 24px;
  }
  .flyer__paper {
    position: relative; width: 100%; height: 100%;
    background: radial-gradient(ellipse at 50% 32%, var(--paper-light) 0%, var(--paper-mid) 60%, var(--paper-edge) 100%);
    border: 2px solid #fff;
  }
  .headline {
    position: absolute; left: 0; right: 0;
    text-align: center;
    font-family: "Alfa Slab One", Georgia, serif;
    font-weight: 400; color: var(--ink);
    transform: scaleX(0.8);
    letter-spacing: 1px;
  }
  .headline--wanted { top: 62px; font-size: 72px; line-height: 1; }
  .headline--reward { top: 388px; font-size: 72px; line-height: 1; }
  .portrait {
    position: absolute; left: 240px; top: 152px;
    width: 210px; height: 205px;
    border-radius: 46% 46% 40% 40%;
    background: radial-gradient(ellipse at 50% 45%, #4a4946 0%, var(--art) 70%);
  }
  .copy {
    position: absolute; left: 53px; width: 597px;
    font-family: "Oswald", "Arial Narrow", sans-serif;
    font-weight: 500; font-size: 17.5px; line-height: 24px;
    color: var(--ink); text-align: justify;
  }
  .copy--description { top: 474px; }
  .copy--notice { top: 592px; }
  .banner {
    position: absolute; left: 38px; top: 745px;
    width: 620px; height: 162px;
  }
  .fine-print {
    position: absolute; left: 0; right: 0; top: 935px;
    text-align: center;
    font-family: "Oswald", "Arial Narrow", sans-serif;
    font-weight: 500; font-size: 16px; color: var(--ink);
  }
</style>
</head>
<body>
  <article class="flyer">
    <div class="flyer__paper">
      <h1 class="headline headline--wanted">WANTED</h1>
      <div class="portrait" role="img" aria-label="Illustration of an outlaw wearing a cowboy hat"></div>
      <h2 class="headline headline--reward">REWARD!</h2>

      <p class="copy copy--description">Desperate person in pain. May look like they have a bad headaech, stiff nech, or low back pain. they may even look like they have a lot of pain between the shoulder blades, a lot of pain between the shoulder blades, at the elbow or knee.</p>

      <p class="copy copy--notice">If you see the person please be adviced they may be grumpy and in need of chiropractic care. There is a reward of a family-sized turkey of any desperate character brought in fitting this description during this month.</p>

      <svg class="banner" viewBox="0 0 620 162" aria-label="Blank area for practice details">
        <polygon points="0,40 90,40 90,158 0,158 48,99" fill="var(--banner)"/>
        <polygon points="530,40 620,40 572,99 620,158 530,158" fill="var(--banner)"/>
        <polygon points="78,133 90,133 90,158" fill="var(--banner-fold)"/>
        <polygon points="530,133 542,133 530,158" fill="var(--banner-fold)"/>
        <rect x="88" y="0" width="444" height="134" fill="var(--banner)"/>
      </svg>

      <p class="fine-print">Offer not valid for Medicare, Worker's Comp. &amp; Personal Injury cases</p>
    </div>
  </article>
</body>
</html>
```